Offshore Energy Projects Management Consultancy needs a business card design

Logo available. We provide teams to deliver engineering consultancy, project management and delivery teams mainly in the offshore renewables sector. The company is all about bringing the right people to a project to deliver the scope.

The business card will be used for all staff.

The business card should be quite simple, vibrant and uncluttered but convey experience, enthusiasm and integration.

Target Market(s)

Energy Project Developers and Tier 1 construction companies

Contact Information for Business Card

Logo should be on the back of the card. I'm happy for the designer to play with the colour of the logo and background colour.

Front of the card should convey all the must have information in a clear and professional manner but without being overly traditional.

Colors

Designer to choose colors to be used in the design.

Requirements
Must have
• Land Line Tel Number, Mobile Tel Number, Email, business address, web address.

```html
<!DOCTYPE html>
<html lang="en">
<head>
<meta charset="utf-8">
<title>Tidewater Works — Business Card</title>
<link rel="stylesheet" href="https://fonts.googleapis.com/css2?family=Montserrat:wght@400;500;600&display=swap">
<style>
  :root {
    --brand-blue: #1677c2;
    --brand-sky: #2ea3e3;
    --ink-grey: #5a5d60;
    --card-white: #ffffff;
    --backdrop: #e9ecef;
  }
  * { box-sizing: border-box; margin: 0; padding: 0; }
  html, body { width: 1200px; height: 912px; overflow: hidden; }
  body {
    background: var(--backdrop);
    font-family: "Montserrat", sans-serif;
    display: flex;
    flex-direction: column;
    align-items: center;
    justify-content: center;
    gap: 60px;
  }
  .card {
    position: relative;
    width: 640px;
    height: 366px;
    border-radius: 22px;
    overflow: hidden;
    box-shadow: 0 6px 18px rgba(0,0,0,0.12);
  }
  .card--back {
    background: var(--brand-blue);
    display: flex;
    align-items: center;
    justify-content: center;
  }
  .wordmark {
    display: flex;
    align-items: center;
    gap: 14px;
  }
  .wordmark__dot {
    width: 30px;
    height: 30px;
    border-radius: 50%;
    flex: none;
  }
  .wordmark__name {
    font-weight: 600;
    font-size: 34px;
    letter-spacing: 0.5px;
    text-transform: uppercase;
    white-space: nowrap;
  }
  .card--back .wordmark__dot { background: var(--card-white); }
  .card--back .wordmark__name { color: var(--card-white); }

  .card--front { background: var(--card-white); }
  .card--front .wordmark {
    position: absolute;
    left: 44px;
    top: 150px;
    gap: 12px;
  }
  .card--front .wordmark__dot { background: var(--brand-blue); width: 22px; height: 22px; }
  .card--front .wordmark__name { color: var(--brand-blue); font-size: 24px; }

  .divider {
    position: absolute;
    left: 378px;
    top: 70px;
    width: 1.5px;
    height: 170px;
    background: var(--brand-blue);
  }
  .contact {
    position: absolute;
    left: 404px;
    top: 58px;
    color: var(--ink-grey);
    font-size: 14px;
    line-height: 1.5;
  }
  .contact__name {
    color: var(--brand-blue);
    font-weight: 600;
    font-size: 21px;
    text-transform: uppercase;
    line-height: 1.1;
  }
  .contact__role { font-size: 14px; margin-bottom: 10px; }
  .contact__address { margin-bottom: 10px; }
  .contact__list { list-style: none; }
  .contact__list li { display: flex; align-items: center; gap: 9px; }
  .contact__list svg { width: 11px; height: 11px; flex: none; }
  .swoosh {
    position: absolute;
    left: 0;
    top: 0;
    width: 640px;
    height: 366px;
  }
</style>
</head>
<body>
  <section class="card card--back" aria-label="Card back">
    <div class="wordmark">
      <span class="wordmark__dot"></span>
      <span class="wordmark__name">Tidewater Works</span>
    </div>
  </section>

  <section class="card card--front" aria-label="Card front">
    <svg class="swoosh" viewBox="0 0 640 366" aria-hidden="true">
      <path d="M335 366 C 430 318, 540 288, 640 272 L 640 366 Z" fill="#1677c2"/>
      <path d="M298 366 C 400 305, 510 272, 628 260 C 520 280, 410 318, 318 366 Z" fill="#2ea3e3"/>
    </svg>

    <div class="wordmark">
      <span class="wordmark__dot"></span>
      <span class="wordmark__name">Tidewater Works</span>
    </div>

    <div class="divider"></div>

    <div class="contact">
      <p class="contact__name">Daniel Hart</p>
      <p class="contact__role">President</p>
      <p class="contact__address">2817 Harbor Lane<br>Portland, ME 04101</p>
      <ul class="contact__list">
        <li>
          <svg viewBox="0 0 12 12"><path d="M2.5 1 L4.5 1 L5.2 3.6 L4 4.6 C4.6 6 6 7.4 7.4 8 L8.4 6.8 L11 7.5 L11 9.5 C11 10.4 10.4 11 9.5 11 C5 11 1 7 1 2.5 C1 1.6 1.6 1 2.5 1 Z" fill="#1677c2"/></svg>
          555-214-7730
        </li>
        <li>
          <svg viewBox="0 0 12 12"><rect x="1" y="2.5" width="10" height="7" rx="1" fill="none" stroke="#1677c2" stroke-width="1.3"/><path d="M1.5 3 L6 6.6 L10.5 3" fill="none" stroke="#1677c2" stroke-width="1.3"/></svg>
          info@veltrax.com
        </li>
        <li>
          <svg viewBox="0 0 12 12"><circle cx="6" cy="6" r="5" fill="none" stroke="#1677c2" stroke-width="1.2"/><ellipse cx="6" cy="6" rx="2.2" ry="5" fill="none" stroke="#1677c2" stroke-width="1"/><path d="M1 6 H11" stroke="#1677c2" stroke-width="1"/></svg>
          www.veltrax.com
        </li>
      </ul>
    </div>
  </section>
</body>
</html>
```